Brenwick Gate Website Design/Content Overhaul

We need to overhaul and modernize www.brenwickgates.example template and layout to fit new content scheme. As part of my package, please code the the design so project can be fully-functional.

All content is provided in attached powerpoint. Feel free to use our sister company's website: www.quintavoreworld.example as a reference.

This website launch is scheduled for March 31st. It is very important that we receive an exceptional website that boosts our credibility and delivers a seamless UX.

I will make sure to be very responsive in accommodating any requests you may have.

Looking forward to a successful project.

Thanks

Target Market(s)

facility managers and procurement departments at fortune 500 companies

Coding

Font styles to use
Sans Serif

Colors
ec1f27
474747

Requirements
Must have
• scrolling logos where necessary
Nice to have
• grayscale logos

```html
<!DOCTYPE html>
<html lang="en">
<head>
<meta charset="utf-8">
<title>Brenwick Gate — Every Entry. Every Dock. Every Day.</title>
<link rel="stylesheet" href="https://fonts.googleapis.com/css2?family=Lato:wght@400;700;900&display=swap">
<style>
:root{
  --red:#ec1f27;
  --ink:#474747;
  --dark:#333333;
  --footer:#2d2d2d;
  --footer-deep:#232323;
  --grey-band:#efefef;
  --rule:#d3d3d3;
  --white:#ffffff;
  --muted:#bdbdbd;
}
*{box-sizing:border-box;margin:0;padding:0}
html,body{width:1200px;height:3536px;overflow:hidden}
body{font-family:"Lato",Arial,sans-serif;color:var(--ink);background:var(--white)}
a{color:inherit;text-decoration:none}
.section-title{font-weight:900;text-transform:uppercase;text-align:center;color:var(--dark);letter-spacing:.3px}
.title-rule{width:76px;height:3px;background:var(--red);margin:14px auto 0}
.pill{display:inline-flex;align-items:center;justify-content:center;border-radius:24px;font-weight:700;text-transform:uppercase;color:var(--white);background:var(--red);font-size:14px;letter-spacing:.4px}

/* top bar */
.top-bar{height:52px;background:var(--dark);display:flex;align-items:center;justify-content:space-between;padding:0 75px;color:var(--white)}
.social{display:flex;gap:12px}
.social span{width:16px;height:16px;border-radius:50%;background:var(--white)}
.call{font-size:17px;font-weight:700;display:flex;align-items:center;gap:10px;letter-spacing:.5px}

/* nav */
.site-nav{height:89px;display:flex;align-items:center;padding:0 75px}
.brand{width:330px}
.brand-name{font-size:36px;font-weight:900;color:var(--ink);line-height:1;letter-spacing:-.3px}
.brand-tag{font-size:11px;font-weight:700;color:var(--ink);margin-top:3px}
.nav-links{display:flex;gap:38px;font-size:13px;font-weight:700;text-transform:uppercase;color:var(--dark)}
.nav-links .active{color:var(--red)}
.nav-demo{margin-left:auto;width:140px;height:40px;font-size:13px}

/* hero */
.hero{position:relative;height:576px;background:linear-gradient(135deg,#4b5258 0%,#2f3337 45%,#6c6f71 100%);text-align:center;color:var(--white)}
.hero-copy{position:absolute;top:196px;left:0;right:0}
.hero h1{font-size:45px;font-weight:900;line-height:46px;text-transform:uppercase}
.hero p{font-size:35px;font-weight:700;line-height:40px;margin-top:8px}
.hero .pill{width:244px;height:46px;margin-top:31px;font-size:14px}
.hero-dots{position:absolute;bottom:30px;left:0;right:0;display:flex;justify-content:center;gap:10px}
.hero-dots span{width:9px;height:9px;border-radius:50%;background:rgba(255,255,255,.55)}
.hero-dots span:first-child{background:var(--white)}

/* problems */
.problems{position:relative;height:756px;padding-top:44px}
.problems .section-title{font-size:33px;line-height:42px}
.problems-copy{position:absolute;top:168px;left:75px;width:1050px;text-align:center;font-size:14.5px;line-height:26px;color:var(--dark)}
.problems-copy p+p{margin-top:10px}
.stats{position:absolute;top:443px;left:75px;display:flex;justify-content:space-between;width:1050px}
.stat{width:330px;height:247px;display:flex;flex-direction:column;align-items:center;justify-content:center;color:var(--white);text-align:center}
.stat-1{background:linear-gradient(160deg,#3c4a57,#1f262d)}
.stat-2{background:linear-gradient(160deg,#6d7378,#3d4246)}
.stat-3{background:linear-gradient(160deg,#4d5a46,#26292a)}
.stat strong{font-size:38px;font-weight:900}
.stat span{font-size:17px;line-height:22px;margin-top:8px}

/* industries */
.industries{height:562px;background:var(--grey-band);padding-top:40px}
.industries .section-title{font-size:30px}
.industry-grid{width:1050px;margin:36px auto 0;display:grid;grid-template-columns:repeat(3,1fr)}
.industry{height:180px;display:flex;flex-direction:column;align-items:center;justify-content:flex-end;gap:22px;font-size:16px;font-weight:700;color:var(--red)}
.industry:nth-child(-n+3){border-bottom:1px solid var(--rule);padding-bottom:44px}
.industry:nth-child(n+4){padding-bottom:12px}
.industry:not(:nth-child(3n)){border-right:1px solid var(--rule)}
.industry:first-child{color:var(--dark)}
.industry svg{width:90px;height:90px}

/* impact */
.impact{height:457px;padding-top:44px}
.impact .section-title{font-size:30px}
.impact-cards{display:flex;justify-content:space-between;width:1052px;margin:48px auto 0}
.impact-card{width:512px;height:255px;display:flex;flex-direction:column;align-items:center;padding-top:80px;color:var(--white)}
.impact-card.industrial{background:linear-gradient(180deg,#5b7286 0%,#3e4c57 60%,#22282c 100%)}
.impact-card.commercial{background:linear-gradient(180deg,#2c3644 0%,#4b5560 55%,#6b665c 100%)}
.impact-card h3{font-size:23px;font-weight:900;text-transform:uppercase}
.impact-card .pill{width:178px;height:42px;margin-top:14px}

/* clients */
.clients{position:relative;height:372px;background:var(--grey-band);padding-top:42px}
.clients .section-title{font-size:30px}
.logo-grid{width:1006px;margin:40px auto 0;display:grid;grid-template-columns:repeat(4,241px);gap:16px 14px}
.logo-tile{height:80px;background:var(--white);border-radius:8px;display:flex;align-items:center;justify-content:center;gap:10px;font-size:23px;font-weight:900;color:var(--ink)}
.logo-tile i{width:14px;height:14px;border-radius:50%;background:var(--ink)}
.arrow{position:absolute;top:226px;width:20px;height:30px}
.arrow.prev{left:56px}.arrow.next{right:56px}

/* cta */
.cta{height:286px;text-align:center;padding-top:44px}
.cta .section-title{font-size:32px}
.cta p{font-size:21px;margin-top:26px;color:var(--dark)}
.cta-actions{display:flex;justify-content:center;align-items:center;gap:14px;margin-top:36px;font-weight:700;font-size:15px;color:var(--dark)}
.cta-actions .pill{width:270px;height:44px}
.cta-actions .pill.alt{background:var(--dark)}

/* footer */
.site-footer{height:316px;background:var(--footer);position:relative;color:var(--white)}
.foot-col{position:absolute;top:44px}
.foot-col h4{font-size:15px;font-weight:900;text-transform:uppercase;margin-bottom:12px}
.foot-col li{list-style:none;font-size:13px;line-height:26px;color:#d8d8d8}
.foot-about{top:196px}
.subscribe-field{width:222px;height:38px;border-radius:19px;background:var(--white);color:#777;font-size:12px;display:flex;align-items:center;padding-left:18px}
.subscribe-btn{width:88px;height:36px;margin:14px 0 0 134px;font-size:13px}
.foot-social{display:flex;gap:18px;margin-top:4px}
.foot-social span{width:18px;height:18px;border-radius:50%;background:var(--white)}
.copyright{height:70px;background:var(--footer-deep);display:flex;align-items:center;justify-content:center;font-size:12px;color:var(--muted)}
</style>
</head>
<body>

<div class="top-bar">
  <div class="social" aria-label="Social links"><span></span><span></span><span></span><span></span><span></span></div>
  <div class="call">
    <svg width="16" height="16" viewBox="0 0 24 24"><path fill="#fff" d="M6.6 10.8a15.1 15.1 0 0 0 6.6 6.6l2.2-2.2c.3-.3.7-.4 1-.2 1.1.4 2.3.6 3.6.6.6 0 1 .4 1 1V20c0 .6-.4 1-1 1A17 17 0 0 1 3 4c0-.6.4-1 1-1h3.5c.6 0 1 .4 1 1 0 1.3.2 2.5.6 3.6.1.3 0 .7-.2 1z"/></svg>
    CALL US NOW 1-800-555-0174
  </div>
</div>

<nav class="site-nav">
  <div class="brand">
    <div class="brand-name">Brenwick Gate</div>
    <div class="brand-tag">Every Entry. Every Dock. Every Day.</div>
  </div>
  <div class="nav-links">
    <a class="active">Home</a><a>Industries</a><a>Services</a><a>Projects</a><a>Resources</a><a>About Us</a>
  </div>
  <a class="pill nav-demo">Get a Demo</a>
</nav>

<header class="hero" role="img" aria-label="Engineers in hard hats reviewing plans at an industrial site">
  <div class="hero-copy">
    <h1>Don’t let docks and doors that have<br>to go slow you down</h1>
    <p>Set the new standard for performance</p>
    <a class="pill">Show me what in store</a>
  </div>
  <div class="hero-dots"><span></span><span></span><span></span><span></span></div>
</header>

<section class="problems">
  <h2 class="section-title">Your problems. Our solutions.<br>The right decision.</h2>
  <div class="title-rule"></div>
  <div class="problems-copy">
    <p>Meeting productivity demands and safety standards for your facilities is hard enough. So, when your door and loading dock equipment wear down and need upgrading, it’s critical to have a trusted industrial and commercial door partner to get you back to full working capacity in no time. However, finding the right partner with the industry credentials and end-to-end experience you’re looking for can be problematic when the majority of providers only offer piecemeal solutions at best.</p>
    <p>That’s where Brenwick Gate™ is a game changer. We take a project-based approach to not only provide you with high performance door technology and equipment – designed to exceed OSHA and other industry-specific safety standards – but also deliver foolproof turnkey solutions that make planning, implementing, and maintaining your equipment across facilities simple.</p>
    <p>Just leave all the heavy-lifting and fine-tuning to us while you get a finished product you can be proud of for years to come.</p>
  </div>
  <div class="stats">
    <div class="stat stat-1" role="img" aria-label="Warehouse interior with loading doors"><strong>100 Yrs.</strong><span>Combined<br>Industry Experience</span></div>
    <div class="stat stat-2" role="img" aria-label="Technician in a hard hat at work"><strong>200K+</strong><span>Installations<br>Across the Northeast</span></div>
    <div class="stat stat-3" role="img" aria-label="Two colleagues in conversation outdoors"><strong>90%</strong><span>Client<br>Retention Rate</span></div>
  </div>
</section>

<section class="industries">
  <h2 class="section-title">A few industries we excel in</h2>
  <div class="title-rule"></div>
  <div class="industry-grid">
    <div class="industry">
      <svg viewBox="0 0 90 90"><ellipse cx="40" cy="36" rx="22" ry="19" fill="#222"/><path d="M52 50 L62 62" stroke="#222" stroke-width="7" stroke-linecap="round"/><circle cx="64" cy="68" r="6" fill="none" stroke="#222" stroke-width="4"/></svg>
      Food &amp; Beverage
    </div>
    <div class="industry">
      <svg viewBox="0 0 90 90" fill="none" stroke="#ec1f27" stroke-width="2.5"><rect x="16" y="34" width="58" height="22" rx="11" transform="rotate(-45 45 45)"/><path d="M35 35 L55 55"/></svg>
      Pharmaceutical
    </div>
    <div class="industry">
      <svg viewBox="0 0 90 90" fill="none" stroke="#ec1f27" stroke-width="2.5"><path d="M12 76V44l16-10v10l16-10v10l16-10V20h10v56z"/><rect x="20" y="54" width="8" height="8"/><rect x="36" y="54" width="8" height="8"/><rect x="52" y="54" width="8" height="8"/><path d="M12 76h66"/></svg>
      Heavy Industry
    </div>
    <div class="industry">
      <svg viewBox="0 0 90 90" fill="none" stroke="#ec1f27" stroke-width="2.5"><path d="M45 12a22 22 0 0 0-13 40v10h26V52a22 22 0 0 0-13-40z"/><path d="M34 68h22M36 74h18M40 62V44l5 5 5-5v18"/></svg>
      Utilities
    </div>
    <div class="industry">
      <svg viewBox="0 0 90 90" fill="none" stroke="#ec1f27" stroke-width="2.5"><path d="M22 28h38v32H22zM60 38h12l8 10v12H60"/><circle cx="32" cy="64" r="6"/><circle cx="68" cy="64" r="6"/><path d="M4 36h12M8 44h10M4 52h12"/></svg>
      Logistics &amp; Distribution
    </div>
    <div class="industry">
      <svg viewBox="0 0 90 90" fill="none" stroke="#ec1f27" stroke-width="2.5"><rect x="22" y="14" width="46" height="56" rx="6"/><path d="M22 48h46M28 22h34v20H28z"/><circle cx="32" cy="58" r="3"/><circle cx="58" cy="58" r="3"/><path d="M30 70v8M60 70v8"/></svg>
      Transportation
    </div>
  </div>
</section>

<section class="impact">
  <h2 class="section-title">Ultimate impact delivered by leading innovation</h2>
  <div class="title-rule"></div>
  <div class="impact-cards">
    <div class="impact-card industrial" role="img" aria-label="Industrial plant with stacks under a blue sky"><h3>Industrial Facilities</h3><a class="pill">That’s me</a></div>
    <div class="impact-card commercial" role="img" aria-label="Commercial building exterior at dusk"><h3>Commercial Facilities</h3><a class="pill">That’s me</a></div>
  </div>
</section>

<section class="clients">
  <h2 class="section-title">A few clients who trust us</h2>
  <div class="title-rule"></div>
  <svg class="arrow prev" viewBox="0 0 20 30"><path d="M14 6 6 15l8 9" fill="none" stroke="#555" stroke-width="3"/></svg>
  <div class="logo-grid">
    <div class="logo-tile">Hollin Foods</div>
    <div class="logo-tile">Verano</div>
    <div class="logo-tile">Aromelle<i></i></div>
    <div class="logo-tile">Ridgefarm</div>
    <div class="logo-tile">Calder Meats</div>
    <div class="logo-tile"><i></i>Fizzwell</div>
    <div class="logo-tile">Brightspring</div>
    <div class="logo-tile">Ostrand Beverage</div>
  </div>
  <svg class="arrow next" viewBox="0 0 20 30"><path d="M6 6l8 9-8 9" fill="none" stroke="#555" stroke-width="3"/></svg>
</section>

<section class="cta">
  <h2 class="section-title">Can we help with your unique situation?</h2>
  <div class="title-rule"></div>
  <p>Let’s have a friendly chat to find out..</p>
  <div class="cta-actions">
    <a class="pill">Give us a call: 1-833-555-0192</a>
    <span>OR</span>
    <a class="pill alt">Get a free consultation</a>
  </div>
</section>

<footer class="site-footer">
  <div class="foot-col" style="left:75px"><h4>Products</h4><ul><li>High Speed Doors</li><li>Rubber Doors</li><li>Pedestrian Doors</li><li>Insect Barrier Doors</li><li>Overhead Doors</li><li>Cold Storage Doors</li><li>Safety Products</li><li>Dock Equipment</li></ul></div>
  <div class="foot-col" style="left:302px"><h4>Industries</h4><ul><li>Food and Beverage</li><li>Pharmaceutical</li><li>Heavy Industry</li><li>Utilities</li><li>Logistics and Distribution</li><li>Transportation</li></ul></div>
  <div class="foot-col" style="left:521px"><h4>Services</h4><ul><li>24 Hour Support</li><li>Preventative Maintenance</li><li>Fire Testing</li><li>Asset ID Tracking</li></ul></div>
  <div class="foot-col" style="left:738px"><h4>Resources</h4><ul><li>Product Guides</li><li>Case Studies</li><li>Videos</li><li>Blog</li></ul></div>
  <div class="foot-col foot-about" style="left:738px"><h4>About</h4><ul><li>Who We Are</li><li>Careers</li><li>Contact Us</li></ul></div>
  <div class="foot-col" style="left:903px">
    <h4>Email Subscribe</h4>
    <div class="subscribe-field">Enter Email Address</div>
    <a class="pill subscribe-btn">Sign up</a>
  </div>
  <div class="foot-col" style="left:903px;top:196px">
    <h4>Follow Us</h4>
    <div class="foot-social"><span></span><span></span><span></span><span></span><span></span></div>
  </div>
</footer>
<div class="copyright">Copyright © 2018 Brenwick Gate Company. All Right Reserved</div>

</body>
</html>
```